Business Card design for law firm = Brindlecourt Australia

We are seeking a new design for our business cards.
We are keeping our logo, which is attached.
We need space for
Name
Title
Address is , which is
Level 14
83 Tarrenby Street
Sydney NSW 2000
Phone :
Mobile :
Fax :
Email :
DX :
website www.brindlecourt.com.au

Industry/Entity Type

Law Firm / Banking and Finance

Contact Information for Business Card

We are seeking a new design for our business cards. We are keeping our logo. We need space for Name Title Address is Level 14 83 Tarrenby Street Sydney NSW 2000 Phone Mobile Fax Email DX website www.brindlecourt.com.au

Colors
0054AA
0677BA
7BADD7
CADEEF
E8F1F8

Requirements
Must have
• see our website for general feel www.brindlecourt.com.au

```html
<!DOCTYPE html>
<html lang="en">
<head>
<meta charset="utf-8">
<title>Brindlecourt Business Card</title>
<link rel="stylesheet" href="https://fonts.googleapis.com/css2?family=EB+Garamond:wght@400&family=Source+Sans+3:wght@400&display=swap">
<style>
  :root {
    --backdrop: #2d2d2f;
    --card-top: #1d1e20;
    --card-bottom: #2a2b2e;
    --brand-blue: #2f4ea3;
    --sky-blue: #0677ba;
    --band-blue: #0a86c4;
    --emboss: #121315;
    --muted: #46484c;
    --white: #ffffff;
  }
  * { margin: 0; padding: 0; box-sizing: border-box; }
  html, body {
    width: 1200px; height: 1138px; overflow: hidden;
    background: var(--backdrop);
  }
  .stage { position: relative; width: 1200px; height: 1138px; }
  .card {
    position: absolute;
    width: 620px; height: 376px;
    border-radius: 16px;
    background: linear-gradient(160deg, var(--card-top), var(--card-bottom));
    overflow: hidden;
  }
  .card--front { left: 272px; top: 184px; }
  .card--back { left: 274px; top: 606px; }

  /* front */
  .front-mark {
    position: absolute; left: 0; right: 0; top: 150px;
    display: flex; align-items: center; justify-content: center; gap: 18px;
  }
  .front-mark__square { width: 58px; height: 58px; background: var(--emboss); }
  .front-mark__name {
    font-family: "EB Garamond", serif; font-size: 56px; line-height: 1;
    color: var(--emboss);
  }

  /* back */
  .brand-square {
    position: absolute; left: 34px; top: 64px; width: 78px; height: 80px;
    background: var(--band-blue);
  }
  .brand-name {
    position: absolute; left: 150px; top: 60px;
    font-family: "EB Garamond", serif; font-size: 52px; line-height: 1;
    color: var(--brand-blue);
  }
  .tagline {
    position: absolute; left: 153px; top: 117px;
    font-family: "Source Sans 3", sans-serif; font-size: 19px; letter-spacing: 1.6px;
    color: var(--sky-blue);
  }
  .person { position: absolute; left: 36px; top: 213px; font-family: "EB Garamond", serif; }
  .person__name { font-size: 26px; line-height: 1.1; color: var(--brand-blue); }
  .person__title { font-size: 16px; color: var(--muted); }
  .address {
    position: absolute; left: 36px; top: 303px;
    font-family: "EB Garamond", serif; font-size: 16px; line-height: 20px; color: var(--muted);
  }
  .contacts {
    position: absolute; left: 316px; top: 212px; list-style: none;
    font-family: "EB Garamond", serif; font-size: 16px; line-height: 20px; color: var(--muted);
  }
  .contacts li { display: flex; align-items: center; gap: 13px; }
  .contacts svg { width: 13px; height: 13px; fill: var(--band-blue); flex: none; }
  .band {
    position: absolute; left: 0; bottom: 0; width: 620px; height: 46px;
  }
  .band__text {
    position: absolute; left: 233px; right: 0; bottom: 0; height: 46px;
    display: flex; align-items: center; justify-content: center;
    font-family: "Source Sans 3", sans-serif; font-size: 16px; letter-spacing: 1.5px;
    color: var(--white);
  }
</style>
</head>
<body>
<main class="stage">
  <section class="card card--front" aria-label="Card front">
    <div class="front-mark">
      <span class="front-mark__square"></span>
      <span class="front-mark__name">Brindlecourt</span>
    </div>
  </section>

  <section class="card card--back" aria-label="Card back">
    <div class="brand-square"></div>
    <div class="brand-name">Brindlecourt</div>
    <div class="tagline">strategic legal outsourcing</div>

    <div class="person">
      <div class="person__name">Liam Hartwell</div>
      <div class="person__title">Managing Director</div>
    </div>

    <address class="address" style="font-style:normal">
      Level 14 83 Tarrenby St<br>Sydney NSW 2000
    </address>

    <ul class="contacts">
      <li><svg viewBox="0 0 16 16"><path d="M2 6c0-2 2-3 6-3s6 1 6 3v1h-3V5.5H5V7H2z M4 8h8l2 6H2z"/></svg>02 9476 0318</li>
      <li><svg viewBox="0 0 16 16"><path d="M4 1h8v4H4z M1 6h14v6h-3v3H4v-3H1z M5 10v4h6v-4z"/></svg>02 9476 0352</li>
      <li><svg viewBox="0 0 16 16"><path d="M1 3h14v10H1z M2 4l6 5 6-5v1l-6 5-6-5z" fill-rule="evenodd"/></svg>liam.hartwell@brindlecourt.com.au</li>
      <li><svg viewBox="0 0 16 16"><path d="M8 1a7 7 0 1 0 0 14A7 7 0 0 0 8 1zm0 1.5c-1 1.2-1.6 3-1.7 4.7h3.4C9.6 5.5 9 3.7 8 2.5zM2.6 7.2h2.3c.1-1.6.5-3.2 1.3-4.4a5.6 5.6 0 0 0-3.6 4.4zm8.5 0h2.3a5.6 5.6 0 0 0-3.6-4.4c.8 1.2 1.2 2.8 1.3 4.4zM2.6 8.8a5.6 5.6 0 0 0 3.6 4.4c-.8-1.2-1.2-2.8-1.3-4.4zm3.7 0c.1 1.7.7 3.5 1.7 4.7 1-1.2 1.6-3 1.7-4.7zm4.8 0c-.1 1.6-.5 3.2-1.3 4.4a5.6 5.6 0 0 0 3.6-4.4z"/></svg>www.brindlecourt.com.au</li>
    </ul>

    <svg class="band" viewBox="0 0 620 46" aria-hidden="true">
      <path d="M258 0H620V46H233Q248 18 258 0z" fill="var(--band-blue)"/>
    </svg>
    <div class="band__text">strategic legal outsourcing</div>
  </section>
</main>
</body>
</html>
```